Glintora.ca Website Build For costume embellishment service

Design a website to promote our business.
Costume embellishing services for Artistic Swimming, Dance, Skating, Gymnastics etc.
We add sparkle to costumes using Velmarent and Quorvela crystals to plain costumes that our customers provide. We also sell new costumes already decorated, Lastly we specialize in reimagining costumes to make them look like new.
We would like samples of our work to be displayed in pictures and video.
We need an information about our services page as well as a contact us page. We have a logo for Glintora which is pink. We like a modern aesthetic as well as bright colours. We are hoping to promote our services worldwide but a big push for Canada. We need to convey that we are Canadian. We would like help with writing copy as well.
We currently have a cartwheel webpage glintora.ca but would like to shut down the cartwheel site as we don't need the payment service. In the new website we will promote payment by CoinLoop or transfer.
A copy of our logo is attached.

Target Market(s)

Athletes and Dancers under 18 years old and parents

Industry/Entity Type

costume embellishment service

Coding

Coded - Design and coding required

Number of Pages Required

4 page

Font styles to use
Sans Serif
Other font styles liked:
• match to the logo for titles

Colors
E54698
E96AAD
F1A4CE
F9D9EA
FCEFF6

Requirements
Must have
• Photos and video upload capability there will be allot of before and after pictures as well as unclose videos.
Nice to have
• modern look I like the look of this website http://www.bramblegallerypier.example
Should not have
• not busy looking

```html
<!DOCTYPE html>
<html lang="en">
<head>
<meta charset="utf-8">
<title>Glintora – Costume Embellishment</title>
<link href="https://fonts.googleapis.com/css2?family=Rubik:wght@400;500;700&family=Karla:wght@400;500;700&family=Great+Vibes&display=swap" rel="stylesheet">
<style>
:root{
  --brand:#b3097f;
  --brand-dark:#9c076e;
  --ink:#1b1b1b;
  --text:#2a2a2a;
  --muted:#444;
  --tint:#f4f0f1;
  --white:#ffffff;
  --rule:#cfcfcf;
}
*{box-sizing:border-box;margin:0;padding:0}
html,body{width:1200px;height:4342px;overflow:hidden}
body{position:relative;background:var(--white);font-family:"Karla",Arial,sans-serif;color:var(--text)}
.abs{position:absolute}
.site-header{left:0;top:0;width:1200px;height:96px;background:var(--brand)}
.brand-name{font-family:"Rubik",Arial,sans-serif;font-weight:500;color:var(--white);font-size:34px;letter-spacing:1px}
.site-header .brand-name{left:130px;top:26px}
.main-nav a{position:absolute;top:38px;color:var(--white);font-family:"Rubik",Arial,sans-serif;font-weight:500;font-size:15px;text-decoration:none;letter-spacing:.5px}
.hero{left:0;top:96px;width:1200px;height:576px;background:linear-gradient(100deg,#1f3b4a 0%,#2d6f86 30%,#476d78 55%,#6b5548 75%,#3a3532 100%)}
.hero-script{left:133px;top:236px;font-family:"Great Vibes",cursive;font-size:100px;color:var(--white);line-height:1}
.hero-title{left:133px;top:350px;font-family:"Rubik",Arial,sans-serif;font-weight:700;font-size:50px;color:var(--white);letter-spacing:1px}
.btn-outline{border:2px solid var(--white);background:var(--brand);color:var(--white);font-family:"Rubik",Arial,sans-serif;font-weight:500;display:flex;align-items:center;justify-content:center;letter-spacing:.5px}
.hero .btn-outline{left:138px;top:345px;width:148px;height:56px;font-size:17px}
.hero-dots{left:563px;top:535px;display:flex;gap:8px;align-items:center}
.hero-dots span{width:7px;height:7px;border-radius:50%;background:var(--white)}
.hero-dots span.active{width:12px;height:12px;background:none;border:2px solid var(--brand)}
.photo{}
.section-title{font-family:"Rubik",Arial,sans-serif;font-weight:500;color:var(--ink);font-size:20px;line-height:1.6;letter-spacing:.3px}
.title-rule{height:3px;background:var(--brand)}
.body-copy{font-size:15.5px;line-height:25px;color:var(--text)}
.body-copy p+p{margin-top:26px}
.tinted{background:var(--tint)}
.how-col{position:absolute;top:1842px;height:342px}
.how-col .icon{position:absolute;top:45px;left:50%;transform:translateX(-50%)}
.how-col p{position:absolute;top:170px;left:0;right:0;text-align:center;font-size:13px;line-height:20px;color:var(--text)}
.vline{position:absolute;top:1842px;width:1px;height:342px;background:var(--rule)}
.btn-solid{background:var(--brand);color:var(--white);display:flex;align-items:center;justify-content:center;font-size:15px}
.band{left:0;top:2844px;width:1200px;height:251px;background:var(--brand)}
.band h2{position:absolute;top:62px;width:100%;text-align:center;font-family:"Rubik",Arial,sans-serif;font-weight:500;color:var(--white);font-size:27px;letter-spacing:.5px}
.band .btn-outline{left:371px;top:130px;width:456px;height:54px;font-size:13.5px;font-weight:700}
.ba-label{position:absolute;font-family:"Rubik",Arial,sans-serif;font-size:13.5px;color:var(--text);text-align:center;width:238px}
.ba-sep{position:absolute;width:1px;background:var(--rule)}
.site-footer{left:0;top:3985px;width:1200px;height:357px;background:var(--brand);color:var(--white)}
.site-footer .brand-name{left:130px;top:85px;font-size:48px}
.foot-head{position:absolute;top:58px;font-family:"Rubik",Arial,sans-serif;font-weight:700;font-size:12.5px;letter-spacing:.5px}
.foot-menu{position:absolute;left:478px;top:95px;list-style:none;font-size:12px;line-height:20px}
.contact-item,.social-item{position:absolute;display:flex;gap:12px;font-size:11.5px;line-height:16px}
.circle{width:22px;height:22px;border-radius:50%;background:var(--white);flex:none;display:flex;align-items:center;justify-content:center;margin-top:2px}
.foot-rule{position:absolute;left:130px;top:278px;width:940px;height:1px;background:rgba(255,255,255,.35)}
.copyright{position:absolute;top:303px;width:100%;text-align:center;font-size:10px}
</style>
</head>
<body>

<header class="site-header abs">
  <div class="brand-name abs">Glintora</div>
  <nav class="main-nav">
    <a style="left:672px">HOME</a>
    <a style="left:775px">IMAGES</a>
    <a style="left:908px">ABOUT US</a>
    <a style="left:1040px">FAQ</a>
  </nav>
</header>

<section class="hero abs" role="img" aria-label="Swimmer in a patterned competition swimsuit adjusting goggles beside an indoor pool">
  <div class="hero-script abs" style="top:140px">Swimming</div>
  <div class="hero-title abs" style="top:254px">COSTUME</div>
  <div class="btn-outline abs">READ MORE</div>
  <div class="hero-dots abs"><span></span><span></span><span class="active"></span><span></span><span></span></div>
</section>

<section>
  <div class="photo abs" role="img" aria-label="Dancer en pointe in a sheer flowing dress against a dark concrete wall" style="left:131px;top:728px;width:469px;height:408px;background:radial-gradient(ellipse at 45% 40%,#6a625a 0%,#3e3934 55%,#242120 100%)"></div>
  <h2 class="section-title abs" style="left:655px;top:760px;width:440px">DAZZLING COMPETITION SUITS AND COSTUMES FOR ALL SPORTS AND EVENTS</h2>
  <div class="title-rule abs" style="left:655px;top:835px;width:108px"></div>
  <div class="body-copy abs" style="left:655px;top:888px;width:410px">
    <p>Create a Dazzling new costume or restyle an existing favourite... no job is too big or too small. Artistic Swimming, Dance, Gymnastics and Skating!</p>
    <p>Our master costume applique designer will work closely with you to fullyunderstand your needs before starting any project.&nbsp; Your satisfaction is our ultimate goal.</p>
  </div>
</section>

<section class="tinted abs" style="left:0;top:1198px;width:1200px;height:474px">
  <h2 class="section-title abs" style="left:131px;top:63px">ORIGINAL COSTUME EMBELLISHMENT</h2>
  <div class="title-rule abs" style="left:131px;top:102px;width:108px"></div>
  <div class="body-copy abs" style="left:131px;top:140px;width:470px">
    <p>Our specialty is design and application, we do not alter the dimensions of the costume or provide any seamstress services.</p>
    <p>Provide the blank canvas (uniform/costume) and we work together on colours, patterns and design.</p>
    <p>We can personalize your swimsuit or costume, by adding Velmarent or Quorvela rhinestones, sequins and embellishments. We can help create that WOW Factor!</p>
  </div>
  <div class="photo abs" role="img" aria-label="Athlete in a black bodysuit stretching beside an aerial hammock on a seaside deck" style="left:659px;top:0;width:541px;height:474px;background:linear-gradient(160deg,#e8e6e3 0%,#d6d3cf 55%,#b9b2aa 100%)"></div>
</section>

<section>
  <h2 class="section-title abs" style="left:0;top:1731px;width:1200px;text-align:center">HOW IT WORKS</h2>
  <div class="title-rule abs" style="left:558px;top:1778px;width:84px"></div>

  <div class="how-col" style="left:128px;width:206px">
    <svg class="icon" width="92" height="86" viewBox="0 0 92 86" fill="none" stroke="#b3097f" stroke-width="3" stroke-linecap="round" stroke-linejoin="round"><rect x="14" y="40" width="64" height="36" rx="3"/><path d="M6 80h80"/><circle cx="46" cy="58" r="5"/><path d="M26 32a20 20 0 0 1 40 0"/><rect x="20" y="26" width="8" height="12" rx="2"/><rect x="64" y="26" width="8" height="12" rx="2"/><path d="M82 8v4M82 18v4M82 28v4"/></svg>
    <p>To start an online consultation, send us a pic of the outfit you want blinged out and we'll get started making colour recommendations and lots of other ideas to get you the result you want.</p>
  </div>
  <div class="vline" style="left:374px"></div>
  <div class="how-col" style="left:400px;width:175px">
    <svg class="icon" width="70" height="80" viewBox="0 0 70 80" fill="none" stroke="#b3097f" stroke-width="3" stroke-linejoin="round"><path d="M22 4h26l14 14v52H22z"/><path d="M48 4v14h14"/><path d="M14 12v64h40"/><path d="M6 20v58h0"/><path d="M30 30h24M30 40h24M30 50h24M30 60h18"/></svg>
    <p>We Will document the process step by step and we will not be happy until you are!</p>
  </div>
  <div class="vline" style="left:600px"></div>
  <div class="how-col" style="left:632px;width:180px">
    <svg class="icon" width="60" height="80" viewBox="0 0 60 80" fill="none" stroke="#b3097f" stroke-width="3" stroke-linejoin="round"><path d="M4 4h52v72l-6-5-7 5-7-5-6 5-7-5-7 5-6-5-6 5z"/><text x="12" y="40" fill="#b3097f" stroke="none" font-family="Rubik,Arial,sans-serif" font-weight="700" font-size="20">$</text><path d="M30 26h18M30 34h18M30 42h18M14 54h34"/></svg>
    <p>Custom Glintora application starts at $150 per item.&nbsp; (Price does not include the price of crystals, sequins or embellishments)</p>
  </div>
  <div class="vline" style="left:841px"></div>
  <div class="how-col" style="left:868px;width:218px">
    <svg class="icon" width="86" height="76" viewBox="0 0 86 76" fill="none" stroke="#b3097f" stroke-width="3" stroke-linejoin="round"><path d="M30 4c2 8 24 8 26 0l26 12-8 18-10-4v42H22V30l-10 4-8-18z"/></svg>
    <p>Upon agreement, send us your outfit and we'll take care of the rest.&nbsp; You can keep track with our progress with shared photos and videos.&nbsp; Upon completion we send back your completed masterpiece.<br>It's that easy!</p>
  </div>

  <div class="btn-solid abs" style="left:332px;top:2248px;width:534px;height:44px">Simply contact us for a no cost consultation by email info@glintora.ca</div>
</section>

<section class="tinted abs" style="left:0;top:2372px;width:1200px;height:472px">
  <div class="photo abs" role="img" aria-label="Figure skater in a purple costume holding a spiral under arena lights" style="left:0;top:0;width:598px;height:472px;background:radial-gradient(ellipse at 50% 50%,#c9d3e3 0%,#6f83a4 40%,#26334d 100%)"></div>
  <h2 class="section-title abs" style="left:684px;top:98px">COSTUME REVITALIZING</h2>
  <div class="title-rule abs" style="left:684px;top:143px;width:108px"></div>
  <div class="body-copy abs" style="left:685px;top:186px;width:370px">
    <p>Restyle or refresh an existing embellished costume by adding new stones to redesign the look.&nbsp; We can also replace missing stones and breathe new life tired or worn outfits.&nbsp; A great option for clubs to inexpensively rejuvenate existing inventory.</p>
  </div>
</section>

<section class="band abs">
  <h2>PURCHASE A READY TO WEAR COSTUME</h2>
  <div class="btn-outline abs">CHOOSE FROM OUR INVENTORY OF COMPLETED COSTUMES</div>
</section>

<section>
  <h2 class="section-title abs" style="left:0;top:3158px;width:1200px;text-align:center">BEFORE AND AFTER</h2>
  <div class="title-rule abs" style="left:565px;top:3205px;width:70px"></div>

  <div class="photo abs" role="img" aria-label="Before: woman in a denim jacket" style="left:108px;top:3259px;width:238px;height:231px;background:linear-gradient(135deg,#a9dbe0,#5c7f9a)"></div>
  <div class="photo abs" role="img" aria-label="After: dancer in a bright yellow costume" style="left:346px;top:3259px;width:239px;height:231px;background:linear-gradient(135deg,#f27c8a,#f4c94a)"></div>
  <div class="photo abs" role="img" aria-label="Before: woman in a floral blouse" style="left:610px;top:3259px;width:238px;height:231px;background:linear-gradient(135deg,#e9e2d6,#4b3b3c)"></div>
  <div class="photo abs" role="img" aria-label="After: skater in a pale blue dress" style="left:848px;top:3259px;width:239px;height:231px;background:radial-gradient(ellipse at 60% 40%,#8b93a0,#2a2e35)"></div>
  <div class="ba-sep" style="left:346px;top:3490px;height:43px"></div>
  <div class="ba-sep" style="left:848px;top:3490px;height:43px"></div>
  <div class="ba-label" style="left:108px;top:3510px">BEFORE</div>
  <div class="ba-label" style="left:346px;top:3510px">AFTER</div>
  <div class="ba-label" style="left:610px;top:3510px">BEFORE</div>
  <div class="ba-label" style="left:848px;top:3510px">AFTER</div>

  <div class="photo abs" role="img" aria-label="Before: woman in a colourful floral dress" style="left:108px;top:3567px;width:238px;height:231px;background:linear-gradient(135deg,#eeeeee,#d88a4f)"></div>
  <div class="photo abs" role="img" aria-label="After: dancer in a sparkling bronze costume" style="left:346px;top:3567px;width:239px;height:231px;background:linear-gradient(135deg,#2c5878,#1a2b38)"></div>
  <div class="photo abs" role="img" aria-label="Before: woman in a light blue knit dress" style="left:610px;top:3567px;width:238px;height:231px;background:linear-gradient(135deg,#22335a,#8fa2d8)"></div>
  <div class="photo abs" role="img" aria-label="After: rhythmic gymnast with a ribbon" style="left:848px;top:3567px;width:239px;height:231px;background:radial-gradient(ellipse at 50% 50%,#5d6fb6,#141b3d)"></div>
  <div class="ba-sep" style="left:346px;top:3798px;height:38px"></div>
  <div class="ba-sep" style="left:848px;top:3798px;height:38px"></div>
  <div class="ba-label" style="left:108px;top:3822px">BEFORE</div>
  <div class="ba-label" style="left:346px;top:3822px">AFTER</div>
  <div class="ba-label" style="left:610px;top:3822px">BEFORE</div>
  <div class="ba-label" style="left:848px;top:3822px">AFTER</div>

  <div class="btn-solid abs" style="left:522px;top:3899px;width:155px;height:37px;font-size:13px;font-family:'Rubik',Arial,sans-serif">VIEW ALL IMAGES</div>
</section>

<footer class="site-footer abs">
  <div class="brand-name abs">Glintora</div>

  <div class="foot-head" style="left:478px">MENU</div>
  <ul class="foot-menu"><li>HOME</li><li>IMAGES</li><li>ABOUT US</li><li>FAQ</li></ul>

  <div class="foot-head" style="left:669px">CONTACT US</div>
  <div class="contact-item" style="left:669px;top:95px"><span class="circle"><svg width="10" height="13" viewBox="0 0 10 13"><path d="M5 0a5 5 0 0 1 5 5c0 4-5 8-5 8S0 9 0 5a5 5 0 0 1 5-5z" fill="#b3097f"/><circle cx="5" cy="5" r="1.8" fill="#fff"/></svg></span><span>2210 Larkspur Lane<br>Maplebrook, ON K2P 0A1</span></div>
  <div class="contact-item" style="left:669px;top:146px"><span class="circle"><svg width="12" height="12" viewBox="0 0 12 12"><path d="M2 1l2.5 0 1 3-1.5 1a7 7 0 0 0 3 3l1-1.5 3 1V10a1 1 0 0 1-1 1A9 9 0 0 1 1 2a1 1 0 0 1 1-1z" fill="#b3097f"/></svg></span><span>Call Us<br>555.014.2736</span></div>
  <div class="contact-item" style="left:669px;top:197px"><span class="circle"><svg width="12" height="9" viewBox="0 0 12 9"><rect width="12" height="9" rx="1" fill="#b3097f"/><path d="M0.5 1l5.5 4 5.5-4" stroke="#fff" fill="none"/></svg></span><span>E mail Us<br>info@glintora.ca</span></div>

  <div class="foot-head" style="left:960px">FOLLOW US</div>
  <div class="social-item" style="left:960px;top:95px"><span class="circle"></span><span>Like us on<br>FRIENDWALL</span></div>
  <div class="social-item" style="left:960px;top:146px"><span class="circle"></span><span>Follow us on<br>CHIRPLINE</span></div>
  <div class="social-item" style="left:960px;top:197px"><span class="circle"></span><span>Follow us on<br>WORKLINK</span></div>

  <div class="foot-rule"></div>
  <div class="copyright">Copyright © 2021 All Rights Reserved</div>
</footer>

</body>
</html>
```